Software engineering company needs business card

I need a cool business card. Company: Soft Belan Brindlewood Ave 41 58207 Sincity Name: Gerald Vanholt CEO / Managing Director & Owner

```html
<!DOCTYPE html>
<html lang="en">
<head>
<meta charset="utf-8">
<title>Soft Belan – Business Card</title>
<link rel="stylesheet" href="https://fonts.googleapis.com/css2?family=Open+Sans:wght@400;600;700&display=swap">
<style>
  :root {
    --backdrop: #2b2622;
    --card: #111111;
    --card-edge: #1c1c1c;
    --green: #8cd11a;
    --white: #f2f2f2;
    --grey: #c9c9c9;
    --divider: #3a3a3a;
  }
  * { margin: 0; padding: 0; box-sizing: border-box; }
  html, body { width: 1200px; height: 900px; overflow: hidden; }
  body {
    background: var(--backdrop);
    font-family: "Open Sans", Arial, sans-serif;
    position: relative;
  }
  .card {
    position: absolute;
    top: 295px;
    width: 540px;
    height: 310px;
    background: var(--card);
    border: 1px solid var(--card-edge);
    box-shadow: 0 18px 40px rgba(0,0,0,0.45);
  }
  .card--front { left: 40px; }
  .card--back { left: 620px; }

  .front__brand {
    position: absolute;
    left: 0; top: 0;
    width: 210px; height: 100%;
    display: flex; align-items: center; justify-content: center;
    gap: 10px;
  }
  .brand-dot {
    width: 14px; height: 14px; border-radius: 50%;
    background: var(--green);
  }
  .brand-name {
    font-weight: 700;
    font-size: 26px;
    color: var(--grey);
    letter-spacing: 0.5px;
  }
  .front__divider {
    position: absolute;
    left: 210px; top: 95px;
    width: 1px; height: 150px;
    background: var(--divider);
  }
  .front__details {
    position: absolute;
    left: 236px; top: 58px;
    color: var(--white);
  }
  .person__name { font-size: 20px; font-weight: 700; line-height: 1.2; }
  .person__first { color: var(--green); }
  .person__title { font-size: 12.5px; color: var(--grey); margin-top: 2px; }
  .company__name { font-size: 18px; font-weight: 700; margin-top: 16px; line-height: 1.2; }
  .company__accent { color: var(--green); }
  .company__address { font-size: 13.5px; color: var(--grey); line-height: 1.35; }
  .contact { list-style: none; margin-top: 14px; font-size: 14px; }
  .contact li { display: flex; align-items: center; gap: 9px; line-height: 1.55; }
  .contact svg { width: 11px; height: 11px; fill: var(--green); flex: none; }

  .back__brand {
    position: absolute; inset: 0;
    display: flex; align-items: center; justify-content: center; gap: 14px;
  }
  .back__brand .brand-name { font-size: 40px; font-weight: 400; letter-spacing: 4px; }
  .back__brand .brand-dot { width: 20px; height: 20px; }
</style>
</head>
<body>
  <section class="card card--front">
    <div class="front__brand">
      <span class="brand-dot"></span>
      <span class="brand-name">Soft Belan</span>
    </div>
    <div class="front__divider"></div>
    <div class="front__details">
      <p class="person__name"><span class="person__first">Gerald</span> Vanholt</p>
      <p class="person__title">CEO / Managing Director &amp; Owner</p>
      <p class="company__name">Soft <span class="company__accent">Belan</span></p>
      <p class="company__address">Brindlewood Ave 41<br>58207 Sincity</p>
      <ul class="contact">
        <li>
          <svg viewBox="0 0 24 24" aria-hidden="true"><path d="M6.6 10.8a15.1 15.1 0 0 0 6.6 6.6l2.2-2.2c.3-.3.7-.4 1-.2 1.1.4 2.3.6 3.6.6.6 0 1 .4 1 1V20c0 .6-.4 1-1 1A17 17 0 0 1 3 4c0-.6.4-1 1-1h3.5c.6 0 1 .4 1 1 0 1.3.2 2.5.6 3.6.1.3 0 .7-.2 1z"/></svg>
          (052)-318-6047
        </li>
        <li>
          <svg viewBox="0 0 24 24" aria-hidden="true"><path d="M2 5h20v14H2z M2 5l10 8 10-8" /></svg>
          info@softbelan.com
        </li>
        <li>
          <svg viewBox="0 0 24 24" aria-hidden="true"><circle cx="12" cy="12" r="11"/></svg>
          www.softbelan.com
        </li>
      </ul>
    </div>
  </section>

  <section class="card card--back">
    <div class="back__brand">
      <span class="brand-dot"></span>
      <span class="brand-name">Soft Belan</span>
    </div>
  </section>
</body>
</html>
```